Facebook Ad design

We need designed a Facebook ad for our solar system's. We want to advertise a 13.32kW system for $4499.

Including: Porvane Heron QX 370W Panels and Kelmora inverters.

```html
<!DOCTYPE html>
<html lang="en">
<head>
<meta charset="utf-8">
<title>Calder Energy – Solar Ad Set</title>
<link rel="stylesheet" href="https://fonts.googleapis.com/css2?family=Montserrat:wght@400;500;700;800&family=Playfair+Display:wght@900&display=swap">
<style>
  :root {
    --board-blue: #2b4aad;
    --brand-red: #b0102a;
    --deep-red: #a90f26;
    --ink-dark: #232838;
    --paper: #e9eef8;
    --white: #ffffff;
  }
  * { box-sizing: border-box; margin: 0; padding: 0; }
  html, body {
    width: 1200px; height: 1004px; overflow: hidden;
    background: var(--board-blue);
    font-family: "Montserrat", sans-serif;
    color: var(--white);
  }
  .board { position: relative; width: 1200px; height: 1004px; }

  .size-label {
    position: absolute; font-size: 17px; font-weight: 400;
    letter-spacing: 0.3px; line-height: 1; text-align: right;
  }
  .size-label.square { right: 610px; top: 30px; }
  .size-label.story { right: 70px; top: 30px; }
  .size-label.wide { right: 615px; top: 590px; }

  .artboard { position: absolute; overflow: hidden; }

  /* brand name lockup */
  .brand { position: absolute; display: flex; flex-direction: column; }
  .brand-row { display: flex; align-items: center; gap: 6px; }
  .brand-mark { width: 16px; height: 16px; background: currentColor; }
  .brand-name {
    font-weight: 700; font-size: 18px; line-height: 0.95;
    letter-spacing: 0.5px; text-transform: uppercase;
  }
  .brand-tagline {
    font-weight: 400; font-size: 7.2px; letter-spacing: 0.1px;
    margin-top: 6px; text-transform: uppercase; white-space: nowrap;
  }

  /* 1080x1080 */
  .ad-square { left: 124px; top: 55px; width: 467px; height: 467px; }
  .ad-square .scene {
    position: absolute; inset: 0 0 5px 0;
    background:
      radial-gradient(ellipse at 35% 62%, rgba(40,50,120,0.35) 0 18%, transparent 32%),
      linear-gradient(170deg, #b0102a 0%, #c22a3c 45%, #c94152 70%, #b8202f 100%);
  }
  .ad-square .base-strip { position: absolute; left: 0; right: 0; bottom: 0; height: 5px; background: var(--ink-dark); }
  .ad-square .brand { left: 34px; top: 18px; color: var(--white); }
  .ad-square .offer { position: absolute; left: 190px; top: 120px; width: 240px; text-align: center; }
  .ad-square .capacity { font-size: 40px; font-weight: 500; line-height: 1; letter-spacing: -1px; }
  .ad-square .capacity small { font-size: 20px; letter-spacing: 0; }
  .ad-square .lead { font-size: 37px; font-weight: 500; line-height: 1; margin-top: 10px; }
  .ad-square .price { position: relative; font-size: 68px; font-weight: 800; line-height: 1; margin-top: 10px; letter-spacing: -1px; }
  .ad-square .price .currency { position: absolute; left: 9px; top: -4px; font-size: 26px; font-weight: 400; }
  .ad-square .spec { font-size: 10px; font-weight: 500; line-height: 1.45; margin-top: 8px; text-transform: uppercase; }

  /* 1080x1920 */
  .ad-story { left: 661px; top: 55px; width: 468px; height: 831px; background: var(--ink-dark); }
  .ad-story .brand { right: 18px; top: 16px; color: var(--white); align-items: flex-start; }
  .ad-story .offer { position: absolute; left: 0; right: 0; top: 88px; text-align: center; }
  .ad-story .capacity { font-size: 51px; font-weight: 500; line-height: 1; letter-spacing: -1.5px; }
  .ad-story .capacity small { font-size: 27px; letter-spacing: 0; }
  .ad-story .lead { font-size: 37px; font-weight: 500; line-height: 1; margin-top: 6px; letter-spacing: 0.5px; }
  .ad-story .price { position: relative; color: var(--brand-red); font-size: 92px; font-weight: 800; line-height: 1; margin-top: 12px; letter-spacing: -2px; padding-left: 12px; }
  .ad-story .price .currency { position: absolute; left: 110px; top: -6px; font-size: 34px; font-weight: 400; letter-spacing: 0; }
  .ad-story .spec { font-size: 12.5px; font-weight: 500; line-height: 1.5; margin-top: 14px; text-transform: uppercase; }
  .ad-story .plans { position: absolute; inset: 0; }
  .ad-story .mount-product {
    position: absolute; left: 190px; top: 392px; width: 230px; height: 165px;
    background: radial-gradient(ellipse at 50% 45%, #35448a 0%, #2a3566 45%, rgba(35,40,56,0) 72%);
  }

  /* 1200x628 */
  .ad-wide { left: 72px; top: 615px; width: 519px; height: 271px; background: var(--paper); }
  .ad-wide .scene {
    position: absolute; left: 200px; top: 0; right: 0; height: 244px;
    background:
      linear-gradient(90deg, var(--paper) 0%, rgba(233,238,248,0) 30%),
      linear-gradient(160deg, #b9cbe6 0%, #ffffff 30%, #5b7fae 55%, #2d5686 75%, #9a9ea4 100%);
  }
  .ad-wide .brand { left: 14px; top: 12px; color: var(--brand-red); }
  .ad-wide .brand-name { font-size: 13px; }
  .ad-wide .brand-mark { width: 12px; height: 12px; }
  .ad-wide .brand-tagline { font-size: 5px; margin-top: 4px; color: var(--ink-dark); }
  .ad-wide .frame { position: absolute; left: 87px; top: 72px; width: 130px; height: 128px; }
  .ad-wide .offer { position: absolute; left: 109px; top: 102px; color: var(--ink-dark); }
  .ad-wide .capacity { font-size: 16px; font-weight: 800; line-height: 1; }
  .ad-wide .lead { font-size: 12.5px; font-weight: 500; margin-top: 7px; letter-spacing: 0.3px; }
  .ad-wide .price { font-family: "Playfair Display", serif; font-size: 27px; font-weight: 900; color: var(--brand-red); line-height: 1; margin-top: 3px; }
  .ad-wide .spec-band {
    position: absolute; left: 0; right: 0; bottom: 0; height: 27px;
    background: var(--ink-dark); display: flex; align-items: center; justify-content: center;
    font-size: 10.5px; font-weight: 500;
  }
</style>
</head>
<body>
<main class="board">

  <span class="size-label square">1080X1080</span>
  <span class="size-label story">1080X1920</span>
  <span class="size-label wide">1200X628</span>

  <!-- Square feed ad -->
  <section class="artboard ad-square">
    <div class="scene" role="img" aria-label="Modern house with rooftop solar and a ground-mounted solar panel, tinted red"></div>
    <div class="base-strip"></div>
    <div class="brand">
      <div class="brand-row"><span class="brand-mark"></span><span class="brand-name">Calder<br>Energy</span></div>
      <span class="brand-tagline">Engineering and economic solutions</span>
    </div>
    <div class="offer">
      <p class="capacity">13.32<small>kW</small></p>
      <p class="lead">System For</p>
      <p class="price"><span class="currency">$</span>4499</p>
      <p class="spec">Porvane Heron QX 370W panels<br>and Kelmora inverters.</p>
    </div>
  </section>

  <!-- Story ad -->
  <section class="artboard ad-story">
    <svg class="plans" width="468" height="831" viewBox="0 0 468 831" role="img" aria-label="Top view of a solar-panelled roof over architectural plans and a calculator">
      <defs>
        <linearGradient id="plansFill" x1="0" y1="0" x2="1" y2="1">
          <stop offset="0" stop-color="#f1f1f1"/>
          <stop offset="0.45" stop-color="#5a5f6e"/>
          <stop offset="0.7" stop-color="#d9c9c6"/>
          <stop offset="1" stop-color="#f4f4f4"/>
        </linearGradient>
      </defs>
      <path d="M88,318 C120,330 150,370 180,420 C220,490 260,545 320,585 C370,615 420,632 468,640 L468,652 C400,640 330,615 270,570 Z" fill="var(--brand-red)"/>
      <path d="M0,318 C40,302 90,308 120,360 C170,440 200,520 270,570 C330,612 400,632 468,650 L468,831 L0,831 Z" fill="url(#plansFill)"/>
    </svg>
    <div class="mount-product" role="img" aria-label="Ground-mounted solar panel on a stand"></div>
    <div class="brand">
      <div class="brand-row"><span class="brand-mark"></span><span class="brand-name">Calder<br>Energy</span></div>
      <span class="brand-tagline">Engineering and economic solutions</span>
    </div>
    <div class="offer">
      <p class="capacity">13.32<small>kW</small></p>
      <p class="lead">SYSTEM FOR</p>
      <p class="price"><span class="currency">$</span>4499</p>
      <p class="spec">Porvane Heron QX 370W panels<br>and Kelmora inverters.</p>
    </div>
  </section>

  <!-- Wide link ad -->
  <section class="artboard ad-wide">
    <div class="scene" role="img" aria-label="Rooftop solar water heater reflecting a blue cloudy sky"></div>
    <div class="brand">
      <div class="brand-row"><span class="brand-mark"></span><span class="brand-name">Calder<br>Energy</span></div>
      <span class="brand-tagline">Engineering and economic solutions</span>
    </div>
    <svg class="frame" width="130" height="128" viewBox="0 0 130 128" aria-hidden="true">
      <path d="M0,0 H118 L112,7 H7 V121 H95 L101,128 H0 Z" fill="var(--brand-red)"/>
      <path d="M123,10 H130 V100 L123,92 Z" fill="var(--brand-red)"/>
    </svg>
    <div class="offer">
      <p class="capacity">13.32kW</p>
      <p class="lead">SYSTEM FOR</p>
      <p class="price">$4499.</p>
    </div>
    <div class="spec-band">Porvane Heron QX 370W Panels and Kelmora inverters.</div>
  </section>

</main>
</body>
</html>
```